Marisol transparent business card

I would like to have a transparent business card created.
A simple yet classy card with
Website www.MarisolPennywhite.com
Phone # 555-417-2936
I would like my full photo on the card as well as my logo.

Target Market(s)

The business card will be printed on transparent card stock.
Www.MarisolPennywhite.com
Phone 555-417-2936
I would like my pic on the card and my logo
Author, Speaker, & Wealth architect

Industry/Entity Type

Business

Contact Information for Business Card

Www.MarisolPennywhite.com
Phone 555-417-2936

Font styles to use
Serif
Decorative
Script

Requirements
Must have
• The business card will be printed on transparent card stock.
• Www.MarisolPennywhite.com
• Phone 555-417-2936
• I would like my pic on the card and my logo
• Author, Speaker, & Wealth architect
Nice to have
• If I could have the tattoo on my pic blurred out or airbrushed over

```html
<!DOCTYPE html>
<html lang="en">
<head>
<meta charset="UTF-8">
<title>Marisol Pennywhite – Business Card</title>
<link rel="stylesheet" href="https://fonts.googleapis.com/css2?family=Great+Vibes&family=Cinzel:wght@600&family=Lato:wght@400&display=swap">
<style>
  :root {
    --page-bg: #e6e6e4;
    --card-bg: rgba(255, 255, 255, 0.72);
    --card-edge: rgba(120, 120, 120, 0.45);
    --gold: #b8922e;
    --gold-light: #d8b85a;
    --gold-dark: #8f6d1c;
    --ink: #1d1d1d;
    --ink-soft: #333333;
    --white: #ffffff;
    --photo-dark: #1a1512;
    --photo-mid: #5a3a28;
    --photo-light: #9a6c4e;
  }
  * { box-sizing: border-box; margin: 0; padding: 0; }
  html, body {
    width: 1200px;
    height: 970px;
    overflow: hidden;
    background: var(--page-bg);
  }
  .canvas {
    position: relative;
    width: 1200px;
    height: 970px;
  }
  .card {
    position: absolute;
    left: 90px;
    top: 202px;
    width: 1020px;
    height: 566px;
    border-radius: 26px;
    background: var(--card-bg);
    border: 1.5px solid var(--card-edge);
    overflow: hidden;
  }
  .portrait {
    position: absolute;
    left: 49px;
    top: 18px;
    width: 412px;
    height: 548px;
    border-radius: 120px 120px 0 0;
    background: linear-gradient(180deg, var(--photo-mid) 0%, var(--photo-light) 30%, var(--photo-dark) 55%, var(--photo-dark) 100%);
  }
  .brand-mark {
    position: absolute;
    left: 666px;
    top: 44px;
    width: 120px;
    height: 120px;
    border: 3px solid var(--gold);
    border-radius: 50%;
    display: flex;
    align-items: center;
    justify-content: center;
  }
  .brand-mark span {
    font-family: "Lato", sans-serif;
    font-size: 19px;
    color: var(--gold);
  }
  .name {
    position: absolute;
    left: 440px;
    width: 580px;
    top: 160px;
    text-align: center;
    font-family: "Great Vibes", cursive;
    font-size: 66px;
    line-height: 1;
    white-space: nowrap;
  }
  .name .first { color: var(--gold); }
  .name .last { color: var(--ink); }
  .tagline {
    position: absolute;
    left: 440px;
    width: 580px;
    top: 234px;
    text-align: center;
    font-family: "Cinzel", serif;
    font-weight: 600;
    font-size: 16.5px;
    color: var(--ink-soft);
    letter-spacing: 0.2px;
  }
  .contact {
    position: absolute;
    left: 440px;
    width: 580px;
    text-align: center;
    font-family: "Lato", sans-serif;
    color: var(--ink-soft);
  }
  .contact svg { display: block; margin: 0 auto 8px; }
  .contact-phone { top: 293px; font-size: 24px; }
  .contact-web { top: 374px; font-size: 23px; }
  .role-band {
    position: absolute;
    left: 374px;
    right: 0;
    top: 474px;
    height: 57px;
    background: linear-gradient(90deg, var(--gold-dark) 0%, var(--gold) 40%, var(--gold-light) 100%);
    display: flex;
    align-items: center;
    justify-content: center;
    padding-left: 60px;
    font-family: "Lato", sans-serif;
    font-size: 24px;
    color: var(--white);
  }
</style>
</head>
<body>
<main class="canvas">
  <section class="card">
    <div class="portrait" role="img" aria-label="Full-length portrait photo of Marisol Pennywhite, arms crossed, in a black dress"></div>

    <div class="brand-mark"><span>Pennywhite</span></div>

    <h1 class="name"><span class="first">Marisol</span> <span class="last">Pennywhite</span></h1>
    <p class="tagline">Live Your Life on Purpose, No Excuses</p>

    <div class="contact contact-phone">
      <svg width="16" height="26" viewBox="0 0 16 26" aria-hidden="true">
        <rect x="1.5" y="1.5" width="13" height="23" rx="2" fill="none" stroke="var(--gold)" stroke-width="2.5"/>
        <circle cx="8" cy="21" r="1.3" fill="var(--gold)"/>
      </svg>
      555-417-2936
    </div>

    <div class="contact contact-web">
      <svg width="24" height="24" viewBox="0 0 24 24" aria-hidden="true">
        <circle cx="12" cy="12" r="10" fill="none" stroke="var(--gold)" stroke-width="2.2"/>
        <ellipse cx="12" cy="12" rx="4.5" ry="10" fill="none" stroke="var(--gold)" stroke-width="1.8"/>
        <line x1="2" y1="12" x2="22" y2="12" stroke="var(--gold)" stroke-width="1.8"/>
      </svg>
      www.MarisolPennywhite.com
    </div>

    <div class="role-band">Author, Speaker, &amp; Wealth architect</div>
  </section>
</main>
</body>
</html>
```